Mondaxe custom business card design

Need a authentic, innovative business card design for a new mobile app business. I am uploading a few screen images from our app for you to view. I would like app design theme to match business card design. I can also send logo images.

```html
<!DOCTYPE html>
<html lang="en">
<head>
<meta charset="utf-8">
<title>Mondaxe Business Card</title>
<link rel="stylesheet" href="https://fonts.googleapis.com/css2?family=Montserrat:wght@700;800&family=Open+Sans:wght@400;600&display=swap">
<style>
  :root {
    --backdrop: #3a312d;
    --card-white: #f7f7f6;
    --card-black: #111111;
    --pattern-tone: #1f1f1f;
    --brand-purple: #6a0f9c;
    --ink-dark: #1c1c1c;
    --ink-grey: #5a5a5a;
    --divider: #e2e2e2;
  }
  html, body {
    margin: 0;
    padding: 0;
    width: 1200px;
    height: 844px;
    overflow: hidden;
    background: var(--backdrop);
  }
  .canvas {
    position: relative;
    width: 1200px;
    height: 844px;
  }
  .card {
    position: absolute;
    top: 273px;
    width: 520px;
    height: 297px;
    border-radius: 3px;
    box-shadow: 0 14px 30px rgba(0,0,0,0.45);
    overflow: hidden;
  }
  .card-front {
    left: 50px;
    background: var(--card-white);
  }
  .card-back {
    left: 630px;
    background: var(--card-black);
  }
  .brand-block {
    position: absolute;
    left: 0;
    top: 0;
    width: 225px;
    height: 297px;
    display: flex;
    flex-direction: column;
    align-items: center;
    justify-content: center;
    gap: 16px;
  }
  .brand-dot {
    width: 96px;
    height: 96px;
    border-radius: 50%;
    background: var(--brand-purple);
  }
  .brand-name {
    font-family: "Montserrat", sans-serif;
    font-weight: 800;
    font-size: 34px;
    color: var(--ink-dark);
    letter-spacing: -0.5px;
  }
  .divider {
    position: absolute;
    left: 225px;
    top: 40px;
    width: 1px;
    height: 150px;
    background: var(--divider);
    box-shadow: -3px 0 8px rgba(0,0,0,0.08);
  }
  .contact-block {
    position: absolute;
    left: 250px;
    top: 48px;
    font-family: "Open Sans", sans-serif;
    color: var(--ink-grey);
  }
  .person-name {
    font-family: "Montserrat", sans-serif;
    font-weight: 700;
    font-size: 19px;
    color: var(--brand-purple);
    margin: 0;
    letter-spacing: 0.5px;
  }
  .person-role {
    font-size: 13px;
    margin: 0 0 6px 0;
  }
  .contact-list {
    list-style: none;
    margin: 0;
    padding: 0;
  }
  .contact-list li {
    display: flex;
    align-items: center;
    gap: 8px;
    font-size: 13.5px;
    line-height: 19px;
  }
  .contact-icon {
    width: 11px;
    height: 11px;
    fill: var(--brand-purple);
    flex: none;
  }
  .address {
    margin: 10px 0 0 19px;
    font-size: 13.5px;
    line-height: 19px;
  }
  .back-pattern {
    position: absolute;
    inset: 0;
    background: radial-gradient(circle at 60% 40%, #262626 0%, var(--pattern-tone) 55%, var(--card-black) 100%);
  }
  .back-mark {
    position: absolute;
    left: 250px;
    top: 138px;
    width: 20px;
    height: 20px;
    border-radius: 50%;
    background: var(--brand-purple);
  }
</style>
</head>
<body>
<main class="canvas">
  <section class="card card-front">
    <div class="brand-block">
      <div class="brand-dot"></div>
      <div class="brand-name">Mondaxe</div>
    </div>
    <div class="divider"></div>
    <div class="contact-block">
      <h1 class="person-name">DANIEL CARTER</h1>
      <p class="person-role">Managing Director</p>
      <ul class="contact-list">
        <li><svg class="contact-icon" viewBox="0 0 12 12"><path d="M2 1h2.5l1 3-1.5 1a6 6 0 0 0 3 3l1-1.5 3 1V10a1 1 0 0 1-1 1A9 9 0 0 1 1 2a1 1 0 0 1 1-1z"/></svg>044-987 654 321</li>
        <li><svg class="contact-icon" viewBox="0 0 12 12"><path d="M3 0h6a1 1 0 0 1 1 1v10a1 1 0 0 1-1 1H3a1 1 0 0 1-1-1V1a1 1 0 0 1 1-1zm0 2v7h6V2zm3 8.2a.6.6 0 1 0 0 .01z"/></svg>044-987 654 321</li>
        <li><svg class="contact-icon" viewBox="0 0 12 12"><path d="M0 2h12v1L6 7 0 3zm0 2.5 6 4 6-4V10H0z"/></svg>hello@mondaxe.app</li>
        <li><svg class="contact-icon" viewBox="0 0 12 12"><circle cx="6" cy="6" r="5.5"/><path d="M1 6h10M6 .5c-2 2-2 9 0 11M6 .5c2 2 2 9 0 11" stroke="#f7f7f6" stroke-width=".8" fill="none"/></svg>www.mondaxe.app</li>
      </ul>
      <p class="address">48 Harbour Lane, Westford<br>Avalonia, 560412.</p>
    </div>
  </section>

  <section class="card card-back">
    <div class="back-pattern" role="img" aria-label="Tonal repeating brand pattern on black"></div>
    <div class="back-mark"></div>
  </section>
</main>
</body>
</html>
```